Pilates trainer needs new website

Summary: I need a new, meaningful website in a 1-page format, but one that can be expanded if necessary. I teach in various studios and in the future also in companies. Therefore, the website should convey growth, joy, uniqueness, workout and a bit of luxury.
The website should be inviting.
Layout:
Introduction what I offer
A bit about me
Option to upload price list and timetable in PDF format
Studio address where I teach
The color scheme should be petrol, gold, and colors that match. Not too dark, please.
My current website www.movewell-brennach.de, new domain is corebalance-studio.com (I have already purchased it)
Logo file attached
I have attached a few suggestions but I am also happy to be surprised.

Target Market(s)

Pilates private and small groups,

Industry/Entity Type

Pilates teacher freelancer

Coding

Coded - Design and coding required

Number of Pages Required

1 page

Requirements
Must have
• Welcoming appearance, about me, pictures, offers, colors from the logo but don't get do dark, more fresh and a bit luxurious
Should not have
• Not too wild and going crazy with colors

```html
<!DOCTYPE html>
<html lang="en">
<head>
<meta charset="utf-8">
<title>Lena Morvath – Pilates</title>
<link href="https://fonts.googleapis.com/css2?family=Cinzel:wght@400;500&family=Great+Vibes&family=Roboto:wght@400;500&display=swap" rel="stylesheet">
<style>
:root{
  --gold:#c59a3f;
  --gold-band:#e9d19a;
  --sand:#f8e2ac;
  --cream:#fdf6e9;
  --ink:#1c2233;
  --text:#2b2b2b;
  --muted:#8a8a8a;
  --black:#050505;
  --white:#ffffff;
}
*{margin:0;padding:0;box-sizing:border-box}
html,body{width:1200px;height:2705px;overflow:hidden;background:var(--white)}
body{position:relative;font-family:'Roboto',sans-serif;color:var(--text)}
.abs{position:absolute}
.caps{font-family:'Cinzel',serif;font-weight:400;color:var(--ink);font-variant:small-caps}
.script{font-family:'Great Vibes',cursive;color:var(--gold)}

/* hero */
.hero-band{left:0;top:0;width:1200px;height:674px;background:linear-gradient(135deg,#ecd6a2,#e4c88a)}
.hero-card{left:112px;top:37px;width:977px;height:600px;background:var(--cream);border-radius:60px}
.brand{left:135px;top:92px;font-family:'Cinzel',serif;font-size:19px;color:var(--gold);line-height:1.2}
.brand-dot{display:inline-block;width:14px;height:14px;border-radius:50%;background:var(--gold);margin-right:8px;vertical-align:-1px}
.hero-title{left:148px;top:225px;font-size:50px;line-height:64px;text-transform:uppercase;letter-spacing:2px}
.hero-title small{font-size:38px}
.hero-script{left:150px;top:330px;font-size:190px;line-height:200px}
.btn{display:flex;align-items:center;gap:14px;padding:0 18px 0 28px;height:50px;border-radius:25px;font-family:'Cinzel',serif;font-size:17px;color:var(--ink);letter-spacing:1px}
.btn::before{content:"";width:3px;height:30px;background:var(--gold)}
.hero-btn{left:421px;top:530px;background:var(--cream)}
.hero-photo{left:616px;top:68px;width:442px;height:538px;border-radius:0 0 40px 40px;background:linear-gradient(160deg,#d9d4cb,#8a7a68 55%,#253250)}
.menu{left:922px;top:47px;width:144px;height:55px;background:var(--white);border-radius:28px 0 0 28px;display:flex;align-items:center;justify-content:center;gap:12px;font-size:16px;color:var(--ink)}

/* about */
.about-shape{left:112px;top:674px;width:472px;height:616px;background:#f9e3ae;border-radius:0 0 236px 236px}
.about-photo{left:40px;top:725px;width:675px;height:530px;border-radius:40% 50% 30% 40%;background:radial-gradient(ellipse at 50% 60%,rgba(140,100,125,.45),rgba(140,100,125,0) 70%)}
.about-portrait{left:390px;top:809px;width:214px;height:214px;border-radius:50%;border:6px solid var(--white);background:linear-gradient(180deg,#e2dfda,#1d1f26 70%)}
.about-title{left:620px;top:752px;font-size:34px;text-transform:uppercase;letter-spacing:2px}
.about-text{left:616px;top:812px;width:470px;font-size:15px;line-height:23.3px}
.signature{left:616px;top:1030px;font-size:72px;line-height:90px}
.sig-role{left:620px;top:1118px;font-family:'Cinzel',serif;font-size:18px;letter-spacing:1.5px;color:var(--ink);text-transform:uppercase}
.leaf{left:995px;top:1024px;width:190px;height:195px;border-radius:50%;background:radial-gradient(circle,rgba(197,154,63,.35),rgba(197,154,63,0) 70%)}

/* training */
.train-title{left:112px;top:1400px;font-size:32px;text-transform:uppercase;letter-spacing:2px}
.train-text{left:112px;top:1452px;width:470px;font-size:15px;line-height:23.3px}
.train-btn{left:113px;top:1652px;background:var(--sand)}
.train-photo{left:615px;top:1408px;width:473px;height:419px;border-radius:236px 236px 0 0;background:linear-gradient(160deg,#b59a76,#3a3f59 70%)}
.info-card{left:112px;top:1745px;width:896px;height:263px;background:var(--white);box-shadow:0 4px 10px rgba(197,154,63,.35)}
.label{font-family:'Cinzel',serif;font-size:21px;color:var(--gold);text-transform:uppercase;letter-spacing:1px}
.prices-label{left:152px;top:1800px}
.price{width:87px;height:87px;border-radius:50%;background:var(--gold);display:flex;flex-direction:column;align-items:center;justify-content:center;color:var(--ink);top:1843px}
.price b{font-size:25px;font-weight:500;line-height:26px}
.price span{font-size:12px}
.loc-label{left:654px;top:1800px}
.loc-text{left:654px;top:1850px;width:340px;font-size:25px;line-height:34px;font-weight:500;color:var(--ink)}

/* footer */
.foot-band{left:0;top:2510px;width:1200px;height:195px;background:var(--black)}
.notch{top:2510px;width:0;height:0;border-top:30px solid #3a3a3a}
.foot-arch{left:423px;top:2121px;width:354px;height:420px;background:#f9e3ae;border-radius:177px 177px 0 0}
.foot-brand{left:423px;top:2330px;width:354px;text-align:center;font-family:'Cinzel',serif;font-size:30px;color:var(--gold);line-height:40px}
.socials{left:530px;top:2466px;display:flex;gap:12px;align-items:center}
.social{width:20px;height:20px;border-radius:50%;border:2px solid var(--ink)}
.social.first{width:44px;height:44px;background:var(--gold);border:none}
.contact{width:260px}
.contact h3{font-family:'Cinzel',serif;font-weight:400;font-size:22px;color:var(--ink);text-transform:uppercase;letter-spacing:1px;border-left:6px solid var(--gold);padding-left:6px;line-height:38px}
.contact ul{list-style:none;margin-top:14px;font-size:14px;color:var(--muted)}
.contact li{display:flex;gap:14px;line-height:27px;margin-bottom:4px}
.contact li svg{flex:none;margin-top:7px}
.foot-nav{left:0;top:2610px;width:1200px;text-align:center;font-size:15px;color:#bfbfbf;letter-spacing:.3px}
.foot-nav span{margin:0 18px}
.copyright{left:0;top:2642px;width:1200px;text-align:center;font-size:15px;color:#bfbfbf}
</style>
</head>
<body>

<!-- Hero -->
<div class="abs hero-band"></div>
<div class="abs hero-card"></div>
<div class="abs brand"><span class="brand-dot"></span>CoreBalance<br>Studio</div>
<h1 class="abs caps hero-title">Beauty<br>Starts With</h1>
<div class="abs script hero-script">Pilates</div>
<div class="abs hero-photo" role="img" aria-label="Trainer smiling while exercising on a studio reformer"></div>
<div class="abs menu">
  <svg width="16" height="13" viewBox="0 0 16 13"><rect width="16" height="2.4" fill="#1c2233"/><rect y="5.3" width="16" height="2.4" fill="#1c2233"/><rect y="10.6" width="16" height="2.4" fill="#1c2233"/></svg>MENU
</div>
<div class="abs btn hero-btn">MORE DETAILS</div>

<!-- About -->
<div class="abs about-shape"></div>
<div class="abs about-photo" role="img" aria-label="Woman in a pilates shoulder bridge with one leg raised"></div>
<div class="abs about-portrait" role="img" aria-label="Portrait of the trainer leaning on a barre"></div>
<h2 class="abs caps about-title">About Me</h2>
<p class="abs about-text">I discovered my love for Pilates several years ago and pretty quickly had the desire to teach this method and convince as many people as possible of its positive effects. I completed my training as a Pilates mat trainer very successfully at Flowline Academy. In order to get to know all facets of Pilates, I trained as a studio trainer, both in the classic Pilates method with The Classic Method Guild and in contemporary Pilates through Northpoint Movement. I am a member of the National Pilates Circle and regularly take part in further training courses.</p>
<div class="abs script signature">Lena Morvath</div>
<div class="abs sig-role">Pilates studio and mat trainer</div>
<div class="abs leaf" role="img" aria-label="Golden leaf ornament"></div>

<!-- Individual training -->
<h2 class="abs caps train-title">Individual Training</h2>
<div class="abs train-text">
  <p>To get to know the Pilates method or because you don't have time to take part in group classes? Are you pursuing a specific training goal, have physical limitations or would you like to try Pilates for the first time as a beginner?</p>
  <p style="margin-top:23px">Then personal training is just right for you.<br>During individual training you are the focus and I can concentrate exclusively on you.</p>
</div>
<div class="abs btn train-btn">MORE DETAILS</div>
<div class="abs train-photo" role="img" aria-label="Trainer performing a teaser exercise on a reformer"></div>

<section class="abs info-card"></section>
<div class="abs label prices-label">Prices:</div>
<div class="abs price" style="left:138px"><b>€250</b><span>Per Month</span></div>
<div class="abs price" style="left:254px"><b>€750</b><span>3 Month</span></div>
<div class="abs price" style="left:370px"><b>€1000</b><span>6 Month</span></div>
<div class="abs price" style="left:486px"><b>€1500</b><span>Per Year</span></div>
<div class="abs label loc-label">Location:</div>
<div class="abs loc-text">Hollfeld industrial area Training opportunity also in Ostermoos</div>

<!-- Footer -->
<div class="abs foot-band"></div>
<div class="abs notch" style="left:390px;border-left:33px solid transparent"></div>
<div class="abs notch" style="left:777px;border-right:33px solid transparent"></div>
<div class="abs foot-arch"></div>
<div class="abs foot-brand">CoreBalance<br>Studio</div>
<div class="abs socials" aria-label="Social links">
  <span class="social first"></span><span class="social"></span><span class="social"></span><span class="social"></span>
</div>

<div class="abs contact" style="left:112px;top:2247px">
  <h3>Lena Morvath</h3>
  <ul>
    <li><svg width="12" height="14" viewBox="0 0 12 14"><path d="M6 0a5 5 0 0 0-5 5c0 4 5 9 5 9s5-5 5-9a5 5 0 0 0-5-5zm0 7a2 2 0 1 1 0-4 2 2 0 0 1 0 4z" fill="#c59a3f"/></svg><span>Lindenweg 12<br>83512 Brennach</span></li>
    <li><svg width="13" height="13" viewBox="0 0 13 13"><path d="M3 0l2 3-1.5 1.5a8 8 0 0 0 5 5L10 8l3 2-1.5 2.5C6 13 0 7 .5 1.5z" fill="#c59a3f"/></svg><span>+49 151 2468013</span></li>
    <li><svg width="13" height="11" viewBox="0 0 13 11"><rect width="13" height="11" rx="1.5" fill="#c59a3f"/><path d="M1 2l5.5 4L12 2" stroke="#fff" fill="none"/></svg><span>info@movewell-brennach.de</span></li>
  </ul>
</div>
<div class="abs contact" style="left:840px;top:2247px">
  <h3>Lena Morvath</h3>
  <ul>
    <li><svg width="12" height="14" viewBox="0 0 12 14"><path d="M6 0a5 5 0 0 0-5 5c0 4 5 9 5 9s5-5 5-9a5 5 0 0 0-5-5zm0 7a2 2 0 1 1 0-4 2 2 0 0 1 0 4z" fill="#c59a3f"/></svg><span>Lindenweg 12<br>83512 Brennach</span></li>
    <li><svg width="13" height="13" viewBox="0 0 13 13"><path d="M3 0l2 3-1.5 1.5a8 8 0 0 0 5 5L10 8l3 2-1.5 2.5C6 13 0 7 .5 1.5z" fill="#c59a3f"/></svg><span>+49 151 2468013</span></li>
    <li><svg width="13" height="11" viewBox="0 0 13 11"><rect width="13" height="11" rx="1.5" fill="#c59a3f"/><path d="M1 2l5.5 4L12 2" stroke="#fff" fill="none"/></svg><span>info@movewell-brennach.de</span></li>
  </ul>
</div>

<nav class="abs foot-nav">HOME<span>|</span>INDIVIDUAL TRAINING<span>|</span>GROUP TRAINING<span>|</span>ABOUT ME<span>|</span>CONTACT</nav>
<div class="abs copyright">Copyright © 2024. Lena Morvath | Pilates Glossary | Privacy Policy | imprint</div>

</body>
</html>
```